Stationary/business card/envelope design for Larkvale Dentalcare

We are located in the foothills of the sierra nevada mountains. We are looking for a beautiful classy modern stationary. We need evelopes and business card design all to flow seamlessly. Envelope design.

Additional office address 4816 Meridian Wy., Suite B, Auburn, CA 95604 Phone: pending Fax: pending.

3 different Drs on each business card:
Helen R. Marsh, DDS
Orla P. Marsh, DDS
Rebecca S. Halvey, DDS

Target Market(s)

Dental patients

Industry/Entity Type

Dental

Contact Information for Business Card

Two sided. See example.

Font styles to use
Sans Serif

Requirements
Must have
• One sided business cards. Need envelope design.
Colors should match existing logo.

Helen R. Marsh, DDS
Orla P. Marsh, DDS
Rebecca S. Halvey, DDS

```html
<!DOCTYPE html>
<html lang="en">
<head>
<meta charset="utf-8">
<title>Larkvale Dentalcare – Stationery</title>
<link href="https://fonts.googleapis.com/css2?family=Open+Sans:wght@400;600;700&display=swap" rel="stylesheet">
<style>
:root{
  --bg:#2c2e33;
  --paper:#ffffff;
  --envelope:#e4e5e6;
  --envelope-edge:#c9cacc;
  --green:#1f5e34;
  --blue:#36b0d6;
  --ink:#2a2a2a;
  --faint:#dceff5;
}
*{box-sizing:border-box;margin:0;padding:0}
html,body{width:1200px;height:842px;overflow:hidden}
body{background:var(--bg);font-family:"Open Sans",Arial,sans-serif;color:var(--ink);position:relative}
.piece{position:absolute;background:var(--paper);overflow:hidden;box-shadow:0 6px 18px rgba(0,0,0,.35)}
.brand{display:flex;align-items:center;gap:6px;color:var(--green);font-weight:700;white-space:nowrap}
.brand-dot{border-radius:50%;background:var(--blue);flex:none}
.band{position:absolute;left:0;right:0;bottom:0;background:var(--green);color:#fff;display:flex;align-items:center;padding-left:14px;font-size:8px}
.faint-mark{position:absolute;border-radius:50%;background:var(--faint)}
.contacts{list-style:none;font-size:7px;line-height:1.35}
.contacts li{display:flex;align-items:flex-start;gap:5px;margin-bottom:3px}
.icon{width:9px;height:9px;background:var(--blue);flex:none;display:flex;align-items:center;justify-content:center}
.icon svg{width:7px;height:7px}

/* small envelope */
.envelope-small{left:40px;top:100px;width:300px;height:200px;background:var(--envelope)}
.envelope-small svg.flap{position:absolute;inset:0}
.envelope-small .brand{position:absolute;left:96px;top:38px;font-size:14px}

/* letterhead */
.letterhead{left:375px;top:90px;width:360px;height:510px}
.letterhead .brand{position:absolute;left:30px;top:30px;font-size:15px}
.letterhead .contacts{position:absolute;left:24px;bottom:52px}
.letterhead .band{height:34px}
.letterhead .faint-mark{width:110px;height:110px;right:28px;bottom:-20px}

/* large envelope */
.envelope-large{left:770px;top:90px;width:400px;height:250px}
.envelope-large .brand{position:absolute;left:22px;top:22px;font-size:15px}
.envelope-large .band{height:36px}
.envelope-large .faint-mark{width:90px;height:90px;right:24px;bottom:10px}

/* business card */
.card{width:190px;height:320px}
.business-card{left:770px;top:390px}
.business-card .brand{position:absolute;right:14px;top:18px;font-size:11px}
.business-card .name{position:absolute;left:14px;top:62px;right:14px;font-size:11px;font-weight:700;color:var(--ink);border-bottom:1px solid var(--green);padding-bottom:3px}
.business-card .title{position:absolute;left:14px;top:84px;font-size:8px;font-weight:600;color:var(--green)}
.business-card .contacts{position:absolute;left:14px;top:108px}
.card .band{height:30px;font-size:7px}
.business-card .faint-mark{width:70px;height:70px;right:16px;bottom:38px}

/* appointment card */
.appointment-card{left:980px;top:390px}
.appointment-card .brand{position:absolute;right:14px;top:14px;font-size:9px}
.appointment-card h2{position:absolute;left:14px;top:40px;font-size:10px;font-weight:700;color:var(--green)}
.schedule{position:absolute;left:14px;top:62px;width:162px;list-style:none;font-size:7px}
.schedule li{display:flex;gap:6px;align-items:flex-end;height:17px}
.schedule .day{width:20px}
.schedule .line{flex:1;border-bottom:1px solid #888;height:10px}
.schedule .at{width:10px}
.schedule .line.short{flex:.8}
.appointment-card .note{position:absolute;left:14px;top:158px;width:160px;font-size:7px;line-height:1.35}
.appointment-card .contacts{position:absolute;left:14px;top:192px}
</style>
</head>
<body>

<!-- small envelope -->
<div class="piece envelope-small">
  <svg class="flap" viewBox="0 0 300 200" width="300" height="200" aria-hidden="true">
    <polygon points="0,0 300,0 150,115" fill="#eeeff0" stroke="var(--envelope-edge)" stroke-width="1"/>
    <polyline points="0,200 120,100" fill="none" stroke="var(--envelope-edge)"/>
    <polyline points="300,200 180,100" fill="none" stroke="var(--envelope-edge)"/>
  </svg>
  <div class="brand"><span class="brand-dot" style="width:14px;height:14px"></span>Larkvale Dentalcare</div>
</div>

<!-- letterhead -->
<div class="piece letterhead">
  <div class="brand"><span class="brand-dot" style="width:16px;height:16px"></span>Larkvale Dentalcare</div>
  <ul class="contacts">
    <li><span class="icon"><svg viewBox="0 0 10 10"><path d="M5 1a3 3 0 0 1 3 3c0 2-3 5-3 5S2 6 2 4a3 3 0 0 1 3-3z" fill="#fff"/></svg></span>2290 Cedar Ridge Road Folsom,<br>California 95631</li>
    <li><span class="icon"><svg viewBox="0 0 10 10"><path d="M5 1a3 3 0 0 1 3 3c0 2-3 5-3 5S2 6 2 4a3 3 0 0 1 3-3z" fill="#fff"/></svg></span>4816 Meridian Wy., Suite B, Auburn,<br>CA 95604</li>
    <li><span class="icon"><svg viewBox="0 0 10 10"><path d="M2 1h2l1 2-1 1a5 5 0 0 0 2 2l1-1 2 1v2c-4 1-8-3-7-7z" fill="#fff"/></svg></span>(916) 555-0142</li>
    <li><span class="icon"><svg viewBox="0 0 10 10"><path d="M2 1h2l1 2-1 1a5 5 0 0 0 2 2l1-1 2 1v2c-4 1-8-3-7-7z" fill="#fff"/></svg></span>(916) 555-0187</li>
    <li><span class="icon"><svg viewBox="0 0 10 10"><rect x="1" y="2.5" width="8" height="5" fill="#fff"/><path d="M1 2.5l4 3 4-3" stroke="var(--blue)" fill="none"/></svg></span>larkvaledentalcare@mailbox.com</li>
  </ul>
  <span class="faint-mark" role="img" aria-label="Faint brand circle decoration"></span>
  <div class="band">Website:www.larkvaledentalcare.com</div>
</div>

<!-- large envelope -->
<div class="piece envelope-large">
  <div class="brand"><span class="brand-dot" style="width:16px;height:16px"></span>Larkvale Dentalcare</div>
  <span class="faint-mark" role="img" aria-label="Faint brand circle decoration"></span>
  <div class="band">Website:www.larkvaledentalcare.com</div>
</div>

<!-- business card -->
<div class="piece card business-card">
  <div class="brand"><span class="brand-dot" style="width:12px;height:12px"></span>Larkvale Dentalcare</div>
  <div class="name">REBECCA S. HALVEY, DDS</div>
  <div class="title">Family &amp; Cosmetic Dentistry</div>
  <ul class="contacts">
    <li><span class="icon"><svg viewBox="0 0 10 10"><path d="M5 1a3 3 0 0 1 3 3c0 2-3 5-3 5S2 6 2 4a3 3 0 0 1 3-3z" fill="#fff"/></svg></span>2290 Cedar Ridge Road Folsom,<br>California 95631</li>
    <li><span class="icon"><svg viewBox="0 0 10 10"><path d="M5 1a3 3 0 0 1 3 3c0 2-3 5-3 5S2 6 2 4a3 3 0 0 1 3-3z" fill="#fff"/></svg></span>4816 Meridian Wy., Suite B,<br>Auburn, CA 95604</li>
    <li><span class="icon"><svg viewBox="0 0 10 10"><path d="M2 1h2l1 2-1 1a5 5 0 0 0 2 2l1-1 2 1v2c-4 1-8-3-7-7z" fill="#fff"/></svg></span>(916) 555-0142</li>
    <li><span class="icon"><svg viewBox="0 0 10 10"><path d="M2 1h2l1 2-1 1a5 5 0 0 0 2 2l1-1 2 1v2c-4 1-8-3-7-7z" fill="#fff"/></svg></span>(916) 555-0187</li>
    <li><span class="icon"><svg viewBox="0 0 10 10"><rect x="1" y="2.5" width="8" height="5" fill="#fff"/><path d="M1 2.5l4 3 4-3" stroke="var(--blue)" fill="none"/></svg></span>larkvaledentalcare@mailbox.com</li>
  </ul>
  <span class="faint-mark" role="img" aria-label="Faint brand circle decoration"></span>
  <div class="band">Website:www.larkvaledentalcare.com</div>
</div>

<!-- appointment card -->
<div class="piece card appointment-card">
  <div class="brand"><span class="brand-dot" style="width:10px;height:10px"></span>Larkvale Dentalcare</div>
  <h2>Has an appointment on</h2>
  <ul class="schedule">
    <li><span class="day">Mon</span><span class="line"></span><span class="at">At</span><span class="line short"></span></li>
    <li><span class="day">Tue</span><span class="line"></span><span class="at">At</span><span class="line short"></span></li>
    <li><span class="day">Wed</span><span class="line"></span><span class="at">At</span><span class="line short"></span></li>
    <li><span class="day">Thu</span><span class="line"></span><span class="at">At</span><span class="line short"></span></li>
    <li><span class="day">Fri</span><span class="line"></span><span class="at">At</span><span class="line short"></span></li>
  </ul>
  <p class="note">If unable to keep appointment kindly give 24 hour notice</p>
  <ul class="contacts">
    <li><span class="icon"><svg viewBox="0 0 10 10"><path d="M2 1h2l1 2-1 1a5 5 0 0 0 2 2l1-1 2 1v2c-4 1-8-3-7-7z" fill="#fff"/></svg></span>(916) 555-0142</li>
    <li><span class="icon"><svg viewBox="0 0 10 10"><path d="M2 1h2l1 2-1 1a5 5 0 0 0 2 2l1-1 2 1v2c-4 1-8-3-7-7z" fill="#fff"/></svg></span>(916) 555-0187</li>
    <li><span class="icon"><svg viewBox="0 0 10 10"><rect x="1" y="2.5" width="8" height="5" fill="#fff"/><path d="M1 2.5l4 3 4-3" stroke="var(--blue)" fill="none"/></svg></span>larkvaledentalcare@mailbox.com</li>
  </ul>
  <div class="band">Website:www.larkvaledentalcare.com</div>
</div>

</body>
</html>
```